Vireo Halden Business Cards

Vireo Halden Luxury Brand Collection is a global representation business focusing on high end luxury. We need business cards to epitomize our global, luxury delivery model.

Target Market(s)

Global Representation in the hospitality industry

Industry/Entity Type

Hospitality

Contact Information for Business Card

name
title
email: first.last@vh-kmt.com
web: www.vh-kmt.com
mobile:

Requirements
Must have
• double sided design
• incorporate logo colours
• have logo prominent
Should not have
• no designs not incorporating logo colours.

```html
<!DOCTYPE html>
<html lang="en">
<head>
<meta charset="utf-8">
<title>Vireo Halden Business Cards</title>
<link rel="stylesheet" href="https://fonts.googleapis.com/css2?family=Tinos:wght@400;700&display=swap">
<style>
  :root {
    --page: #e8e3d8;
    --gold-light: #ac9653;
    --gold-mid: #9c8647;
    --gold-dark: #85713a;
    --paper: #ffffff;
    --ink-light: #f7f3e8;
    --map-tone: rgba(236, 226, 190, 0.28);
  }
  * { box-sizing: border-box; margin: 0; padding: 0; }
  html, body {
    width: 1200px; height: 780px; overflow: hidden;
    background: var(--page);
    font-family: "Tinos", "Times New Roman", serif;
  }
  .sheet {
    width: 1200px; height: 780px;
    display: flex; align-items: center; justify-content: center; gap: 44px;
  }
  .card {
    position: relative;
    width: 540px; height: 310px;
    overflow: hidden;
    background: linear-gradient(135deg, var(--gold-light), var(--gold-mid) 55%, var(--gold-dark));
    box-shadow: 0 6px 18px rgba(60, 48, 20, 0.25);
  }

  /* Front */
  .front-panel {
    position: absolute; top: 0; right: 0;
    width: 300px; height: 175px;
  }
  .front-panel svg { display: block; }
  .front-brand {
    position: absolute; top: 62px; right: 34px;
    width: 220px; text-align: center;
    color: var(--gold-mid);
    font-size: 30px; letter-spacing: 2px; text-transform: uppercase;
    line-height: 1.1;
  }
  .front-text {
    position: absolute; left: 34px; bottom: 28px;
    color: var(--ink-light);
  }
  .company-name {
    font-size: 30px; letter-spacing: 1px; text-transform: uppercase; line-height: 1;
  }
  .company-line {
    font-size: 15px; letter-spacing: 1.2px; text-transform: uppercase; margin-top: 4px;
  }
  .person { margin-top: 22px; }
  .person-name { font-size: 14px; font-weight: 700; text-transform: uppercase; letter-spacing: 0.5px; }
  .person-title { font-size: 13px; }
  .contact { margin-top: 14px; font-size: 13px; line-height: 1.4; }
  .contact-row { display: flex; align-items: center; gap: 7px; }
  .contact-row svg { flex: none; }
  .web { letter-spacing: 2px; }
  .web b { font-weight: 700; }

  /* Back */
  .map-area {
    position: absolute; left: 60px; top: 30px; width: 420px; height: 250px;
    border-radius: 48% 52% 46% 54%;
    background: radial-gradient(ellipse at center, var(--map-tone), rgba(236, 226, 190, 0.08) 70%, transparent 75%);
  }
  .back-brand {
    position: absolute; left: 0; right: 0; top: 118px;
    text-align: center; color: var(--paper);
  }
  .back-name { font-size: 42px; letter-spacing: 3px; text-transform: uppercase; line-height: 1; }
  .back-tagline { margin-top: 10px; font-size: 13px; letter-spacing: 2px; text-transform: uppercase; }
</style>
</head>
<body>
<main class="sheet">

  <section class="card card-front" aria-label="Business card front">
    <div class="front-panel">
      <svg width="300" height="175" viewBox="0 0 300 175" aria-hidden="true">
        <path d="M30 0 H300 V175 H120 C60 175 30 120 30 60 Z" fill="var(--paper)"/>
      </svg>
    </div>
    <div class="front-brand">Vireo Halden</div>

    <div class="front-text">
      <div class="company-name">Vireo Halden</div>
      <div class="company-line">Luxury Brand Collection</div>

      <div class="person">
        <div class="person-name">Elias Morrow</div>
        <div class="person-title">Director</div>
      </div>

      <div class="contact">
        <div>PO BOX 274, Alder Street</div>
        <div>3rd Lane, Nevada</div>
        <div class="contact-row">
          <svg width="10" height="10" viewBox="0 0 10 10" aria-hidden="true"><rect x="1" y="1" width="8" height="8" fill="none" stroke="currentColor"/></svg>
          <span>(555) 014 2378</span>
        </div>
        <div class="contact-row">
          <svg width="10" height="10" viewBox="0 0 10 10" aria-hidden="true"><rect x="0.5" y="2" width="9" height="6" fill="none" stroke="currentColor"/><path d="M0.5 2 L5 6 L9.5 2" fill="none" stroke="currentColor"/></svg>
          <span>first.last@vh-kmt.com</span>
        </div>
        <div class="contact-row web">
          <svg width="10" height="10" viewBox="0 0 10 10" aria-hidden="true"><circle cx="5" cy="5" r="4.5" fill="currentColor"/></svg>
          <span>www.<b>vh-kmt</b>.com</span>
        </div>
      </div>
    </div>
  </section>

  <section class="card card-back" aria-label="Business card back">
    <div class="map-area" role="img" aria-label="Faint world map in light gold tones"></div>
    <div class="back-brand">
      <div class="back-name">Vireo Halden</div>
      <div class="back-tagline">Luxury Brands Collection</div>
    </div>
  </section>

</main>
</body>
</html>
```